Business Card Design Project

Velvet Harbor is a Boutique Clothing. On the business cards I would like to have this included
Website: www.velvetharbor-example.com
Email: shop@velvetharbor-example.com
Owner: Mira Sol & Tor Dell

Industry/Entity Type

Business

Contact Information for Business Card

I wanted something simple and elegant. I have attach business logo.

```html
<!DOCTYPE html>
<html lang="en">
<head>
<meta charset="utf-8">
<title>Velvet Harbor Business Card</title>
<link href="https://fonts.googleapis.com/css2?family=Open+Sans:wght@400;600&family=Roboto+Condensed:wght@500;700&display=swap" rel="stylesheet">
<style>
  :root {
    --backdrop: #a7a7a7;
    --card-dark: #121212;
    --card-light: #f4f4f4;
    --ink-light: #f2f2f2;
    --ink-dark: #2e2e2e;
    --ink-muted: #555555;
    --rule: #9a9a9a;
  }
  html, body {
    margin: 0;
    padding: 0;
    width: 1200px;
    height: 960px;
    overflow: hidden;
    background: var(--backdrop);
  }
  .canvas {
    position: relative;
    width: 1200px;
    height: 960px;
  }
  .card {
    position: absolute;
    left: 320px;
    width: 600px;
    height: 342px;
  }
  .card--front {
    top: 110px;
    background: var(--card-dark);
  }
  .card--back {
    top: 493px;
    background: var(--card-light);
  }
  .brand-name {
    position: absolute;
    font-family: "Open Sans", sans-serif;
    font-weight: 400;
    letter-spacing: 6px;
    text-transform: uppercase;
    text-align: center;
    white-space: nowrap;
    transform: translate(-50%, -50%);
  }
  .card--front .brand-name {
    left: 295px;
    top: 160px;
    font-size: 24px;
    color: var(--ink-light);
  }
  .card--back .brand-name {
    left: 162px;
    top: 172px;
    font-size: 18px;
    letter-spacing: 4px;
    color: var(--ink-dark);
  }
  .divider {
    position: absolute;
    left: 272px;
    top: 85px;
    width: 1px;
    height: 158px;
    background: var(--rule);
  }
  .contact {
    position: absolute;
    left: 302px;
    top: 96px;
  }
  .owners {
    margin: 0;
    font-family: "Roboto Condensed", sans-serif;
    font-weight: 700;
    font-size: 22px;
    color: var(--ink-dark);
    text-transform: uppercase;
    line-height: 1;
  }
  .role {
    margin: 6px 0 0;
    font-family: "Roboto Condensed", sans-serif;
    font-weight: 500;
    font-size: 15px;
    color: var(--ink-dark);
    text-transform: uppercase;
  }
  .details {
    margin: 14px 0 0;
    font-family: "Open Sans", sans-serif;
    font-size: 14px;
    line-height: 20px;
    color: var(--ink-muted);
  }
  .social {
    display: block;
    margin-top: 18px;
  }
</style>
</head>
<body>
  <main class="canvas">
    <section class="card card--front">
      <span class="brand-name">Velvet Harbor</span>
    </section>

    <section class="card card--back">
      <span class="brand-name">Velvet Harbor</span>
      <div class="divider"></div>
      <div class="contact">
        <h1 class="owners">Mira Sol &amp; Tor Dell</h1>
        <p class="role">Owner</p>
        <p class="details">shop@velvetharbor-example.com<br>www.velvetharbor-example.com</p>
        <svg class="social" width="90" height="28" viewBox="0 0 90 28" aria-hidden="true">
          <circle cx="13" cy="14" r="13" fill="#2e2e2e"/>
          <circle cx="43" cy="14" r="13" fill="#2e2e2e"/>
          <circle cx="73" cy="14" r="13" fill="#2e2e2e"/>
        </svg>
      </div>
    </section>
  </main>
</body>
</html>
```